Modern Banner and Window Decal Design For Law Firm Lawyer

We are looking for three modern and sophisticated banner design and window decal for our law firm.

Banner measurements/types:

1) Height: 130 cm Width: 160 cm (Outdoor banner)
2) Height: 200 cm Width: 85 cm (Pull up/retractable indoor banner)

Window Decal:
3) Height: 70cm width 70cm

Our law firm is based in Melbourne, Australia and we deal with property law mostly.

We prefer a white background with classic text in black or grey. We would also like a dash of colour so please use a green, blue or aqua colour palette that is consistent with our logo. Vector attached. A nice photo of property, Melbourne city viee, or family home would be nice.

We do not want any law related images - scales of justice, gavel or the like.

Our ultimate goal is to communicate that the firm is modern, professional and knowledgeable

We would like the following:

1. Our logo
2. Our services: - Property Law - Wills - Powers of Attorney - Probate - Estate Administration - Consultancy & Agency
3. Phone number
4. Web Address

5. For pull up/retractable banner we would also like the following text:

We use the latest digital technology and fixed-fees to provide fast and affordable legal advice that is easy to understand.

For privacy reasons, we will provide business details once we have decided on the winner.

We will monitor entries closely and promise to provide feedback and guidance on each entry.

Thank you very much for considering this project.

Target Market(s)

General public, professionals, lawyers and conveyancers

Industry/Entity Type

Law Firm

Font styles to use
Sans Serif

Colors
0393ce
34a6d7
0456a4
3176b5
acd037
33b8a4
86cfc6
00a990
9ccb3b

Requirements
Must have
• 1. Our logo
• 2. Our services: - Property Law - Wills - Powers of Attorney - Probate & Estate Administration - Consultancy & Agency
• 3. Phone number
• 4. Web Address
Nice to have
• Picture of Melbourne, Australia city ; property/buildings/lawyers
Should not have
• We do not want any law related images - scales of justice, gavel or the like.

```html
<!DOCTYPE html>
<html lang="en">
<head>
<meta charset="utf-8">
<title>Ridgeway Lawyers – Banner Set</title>
<link rel="stylesheet" href="https://fonts.googleapis.com/css2?family=Lato:ital,wght@0,400;0,700;0,900;1,700&display=swap">
<style>
  :root {
    --ink: #1f1f1f;
    --heading: #2e4a2a;
    --brand-text: #3a3f4a;
    --sky: #29b6e8;
    --lime: #acd037;
    --lime-soft: #c9e36a;
    --aqua: #86cfc6;
    --bullet: #8fd3e8;
    --frame: #6a6a6a;
    --white: #ffffff;
  }
  * { margin: 0; padding: 0; box-sizing: border-box; }
  html, body { width: 1200px; height: 964px; overflow: hidden; background: var(--white); }
  body { position: relative; font-family: "Lato", sans-serif; color: var(--ink); }

  .size-label {
    position: absolute; font-weight: 900; font-size: 44px; color: var(--heading);
    letter-spacing: 0.5px; white-space: nowrap; transform: translateX(-50%);
  }
  .size-label--outdoor { left: 388px; top: 318px; }
  .size-label--pullup { left: 902px; top: 46px; }

  .banner { position: absolute; background: var(--white); border: 1.5px solid var(--frame); overflow: hidden; }
  .banner--outdoor { left: 78px; top: 385px; width: 624px; height: 508px; }
  .banner--pullup { left: 740px; top: 112px; width: 332px; height: 783px; }

  .brand { position: absolute; display: flex; align-items: center; gap: 10px; }
  .brand__mark { width: 80px; height: 80px; border-radius: 50%; border: 6px solid var(--aqua); flex: none; }
  .brand__name { color: var(--brand-text); font-weight: 400; line-height: 1.1; }
  .brand__name span { display: block; }
  .brand__line1 { font-size: 23px; letter-spacing: 0.5px; }
  .brand__line2 { font-size: 17px; letter-spacing: 1.5px; }
  .banner--outdoor .brand { left: 22px; top: 22px; }
  .banner--pullup .brand { left: 25px; top: 25px; }

  .city-photo {
    position: absolute; border-radius: 50%; border: 2px solid var(--sky);
    background: radial-gradient(ellipse at 50% 40%, #3c5fb0 0%, #1b2d66 55%, #0c1533 100%);
  }
  .banner--outdoor .city-photo { left: 364px; top: 32px; width: 176px; height: 78px; }
  .banner--pullup .city-photo { left: 65px; top: 565px; width: 192px; height: 90px; }

  .services { position: absolute; list-style: none; font-weight: 700; }
  .services li { display: flex; align-items: center; }
  .services li::before {
    content: ""; flex: none; border-radius: 50%;
    border: 3px dotted var(--bullet);
  }
  .banner--outdoor .services { left: 38px; top: 143px; font-size: 29px; }
  .banner--outdoor .services li { height: 45px; }
  .banner--outdoor .services li::before { width: 20px; height: 20px; margin-right: 16px; }
  .banner--pullup .services { left: 25px; top: 150px; font-size: 22px; }
  .banner--pullup .services li { height: 33px; }
  .banner--pullup .services li::before { width: 16px; height: 16px; margin-right: 12px; }

  .divider { position: absolute; height: 3px; background: var(--lime); }
  .divider--a { left: 22px; top: 374px; width: 180px; }
  .divider--b { left: 130px; top: 382px; width: 177px; }

  .tagline {
    position: absolute; left: 0; width: 100%; top: 408px; text-align: center;
    font-size: 21px; font-weight: 700; font-style: italic; line-height: 32px;
  }

  .footer { position: absolute; left: 0; bottom: 0; width: 100%; }
  .footer svg { position: absolute; left: 0; top: 0; width: 100%; }
  .footer__text { position: absolute; left: 0; width: 100%; color: var(--white); }
  .banner--outdoor .footer { height: 90px; }
  .banner--outdoor .footer__text {
    bottom: 12px; display: flex; justify-content: space-between; padding: 0 30px; font-size: 22px;
  }
  .banner--pullup .footer { height: 100px; }
  .banner--pullup .footer__text { bottom: 6px; text-align: center; }
  .footer__phone { font-size: 27px; display: block; }
  .footer__web { font-size: 21px; display: block; }
  .banner--outdoor .footer__phone, .banner--outdoor .footer__web { font-size: 22px; }
  .footer b { font-weight: 700; }
</style>
</head>
<body>
  <div class="size-label size-label--outdoor">1.60 X 1.30 MTS.</div>
  <div class="size-label size-label--pullup">2 MTS. X 85 CM.</div>

  <section class="banner banner--outdoor">
    <div class="brand">
      <div class="brand__mark"></div>
      <div class="brand__name"><span class="brand__line1">RIDGEWAY</span><span class="brand__line2">LAWYERS</span></div>
    </div>
    <div class="city-photo" role="img" aria-label="Melbourne city skyline at night reflected on the river"></div>
    <ul class="services">
      <li>Property Law.</li>
      <li>Wills.</li>
      <li>Powers of Attorney.</li>
      <li>Probate.</li>
      <li>Estate Administration.</li>
      <li>Consultancy &amp; Agency.</li>
    </ul>
    <div class="footer">
      <svg viewBox="0 0 624 90" preserveAspectRatio="none" height="90">
        <path d="M0 8 Q312 -6 624 8 L624 16 Q312 2 0 16 Z" fill="var(--lime-soft)"/>
        <path d="M0 16 Q312 2 624 16 L624 90 L0 90 Z" fill="var(--sky)"/>
      </svg>
      <div class="footer__text">
        <span class="footer__phone">Phone: <b>0000-0000</b></span>
        <span class="footer__web">Web Site: <b>www.example.com</b></span>
      </div>
    </div>
  </section>

  <section class="banner banner--pullup">
    <div class="brand">
      <div class="brand__mark"></div>
      <div class="brand__name"><span class="brand__line1">RIDGEWAY</span><span class="brand__line2">LAWYERS</span></div>
    </div>
    <ul class="services">
      <li>Property Law.</li>
      <li>Wills.</li>
      <li>Powers of Attorney.</li>
      <li>Probate.</li>
      <li>Estate Administration.</li>
      <li>Consultancy &amp; Agency.</li>
    </ul>
    <div class="divider divider--a"></div>
    <div class="divider divider--b"></div>
    <p class="tagline">We use the latest digital<br>technology and fixed-fees<br>to provide fast<br>and affordable legal</p>
    <div class="city-photo" role="img" aria-label="Melbourne city skyline at night reflected on the river"></div>
    <div class="footer">
      <svg viewBox="0 0 332 100" preserveAspectRatio="none" height="100">
        <path d="M0 6 Q166 -4 332 6 L332 14 Q166 4 0 14 Z" fill="var(--lime-soft)"/>
        <path d="M0 14 Q166 4 332 14 L332 100 L0 100 Z" fill="var(--sky)"/>
      </svg>
      <div class="footer__text">
        <span class="footer__phone">Phone: <b>0000-0000</b></span>
        <span class="footer__web">Web Site: <b>www.example.com</b></span>
      </div>
    </div>
  </section>
</body>
</html>
```